Book cover for a book about time management for women

We need a book cover for a book about time management for women written by a woman. Even though the book has a provocative title "Calendar candy" based on the seminars the author holds for women seeking the change in their life, it has nothing to do with the words themselves. The subtitle is "Keep each morning in your grip. A bold guide on daily rhythm for ladies today"

Preferred fonts (not necessarily):
Plus Jakarta Sans
Tiempos Headline

Preferred colours (not necessarily):
- orange
- pastel "highlighters"

We look for a simple/clean design that catches the attention of the women without too many graphic elements.

Target Market(s)

Women that want to change and organise their life

Industry/Entity Type

productivity, marketing, work-life balance

Font styles to use
Other font styles liked:
• Plus Jakarta Sans, Tiempos Headline

Colors
F0912C
F2A743
F7CA91
FBE8D2
FDF5EE
A7469A
B969AE
D3A5CF
EDDBEB
F8F0F9

Requirements
Must have
• Famine feeling as the target audience are women with drive to better life
Should not have
• No explicit images or sexually motivated themes

```html
<!DOCTYPE html>
<html lang="en">
<head>
<meta charset="utf-8">
<title>Calendar Candy — Book Cover</title>
<link rel="stylesheet" href="https://fonts.googleapis.com/css2?family=Poppins:wght@700;800&family=Yellowtail&display=swap">
<style>
  :root {
    --cover-pink: #e8b6d6;
    --ink: #0b0508;
    --plum-deep: #2a0a22;
    --plum-soft: #5a2a52;
    --subtitle-pink: #f3d6ec;
  }
  * { margin: 0; padding: 0; box-sizing: border-box; }
  html, body { width: 800px; height: 1200px; overflow: hidden; }
  body { background: var(--cover-pink); }

  .cover {
    position: relative;
    width: 800px;
    height: 1200px;
    background: var(--cover-pink);
    overflow: hidden;
    font-family: "Poppins", Arial, sans-serif;
  }

  .author-name {
    position: absolute;
    top: 34px;
    left: 0;
    width: 800px;
    text-align: center;
    font-weight: 700;
    font-size: 35px;
    letter-spacing: 0.5px;
    color: var(--ink);
  }

  .portrait-art {
    position: absolute;
    left: 55px;
    top: 100px;
    width: 690px;
    height: 1040px;
    border-radius: 48% 48% 6% 30% / 32% 32% 4% 12%;
    background: linear-gradient(180deg, var(--ink) 0%, var(--ink) 45%, var(--plum-deep) 80%, var(--plum-soft) 100%);
  }

  .title {
    position: absolute;
    left: 100px;
    width: 640px;
    text-align: center;
    color: var(--cover-pink);
    font-weight: 800;
    line-height: 1;
  }
  .title-top {
    top: 372px;
    font-size: 54px;
    letter-spacing: 1px;
  }
  .title-main {
    top: 428px;
    font-size: 150px;
    letter-spacing: 2px;
  }

  .subtitle {
    position: absolute;
    top: 610px;
    left: 170px;
    width: 500px;
    text-align: center;
    font-family: "Yellowtail", cursive;
    font-size: 38px;
    line-height: 59px;
    color: var(--subtitle-pink);
  }
</style>
</head>
<body>
  <main class="cover">
    <p class="author-name">AUTHOR NAME</p>

    <div class="portrait-art" role="img" aria-label="Black silhouette of a woman's head in profile with flowing hair, fading into a city skyline at the base"></div>

    <h1>
      <span class="title title-top">CALENDAR</span>
      <span class="title title-main">CANDY</span>
    </h1>

    <p class="subtitle">Keep each morning in your grip.<br>A bold guide on daily rhythm<br>for ladies today.</p>
  </main>
</body>
</html>
```